Packaging & Label Design for CDB Products

We are a European CBD company specialising in athletic recovery, sleep improvement and wellness.

We would like the packaging to incorporate our logo and name (and font 'Codec') 'Meridell CBD'. The design must be transferable to all of our products. CBD Oils, Balms, Lip Balm and Vape E-Liquid.

We would like it to be simple but eye-catching and modern. We don't want bright colours. Preferred pallet of muted greys, blacks, white and pastel colours. Geometric concepts, possibly using different colours for each item of the range, we are open to new and fresh ideas (we are seeking you for your experience) and when we find the right design we would likely throw more work in your direction..

Our product range is not complete so the designer must be flexible with some changes and provide files where format can be easily edited by packaging manufacturer. We are also waiting for dimensions for the labels and boxes for several products and will supply the designer with full dimensions of all products once selected.

Oil Box: 2.6 x 9.0 x 2.6 cm (open format 16.7 x 11.6cm)
Labels: 7.8 x 3.3 cm (Front and Back)

Our expected product range will be:
CBD Oil 1000mg
CBD Oil 3000mg
CBD Balm 100mg
CBD Balm 300mg
E-Liquid 500mg
Lip Balm 50mg

We look forward to seeing your ideas.

Best Regards
Meridell CBD

```html
<!DOCTYPE html>
<html lang="en">
<head>
<meta charset="utf-8">
<title>Meridell CBD – CBD Oil 1000mg packaging</title>
<link rel="stylesheet" href="https://fonts.googleapis.com/css2?family=Montserrat:wght@300;400;600;700;800&display=swap">
<style>
  :root {
    --ink: #1c1c1c;
    --charcoal: #4b4b4d;
    --mid-grey: #808083;
    --pale-grey: #e6e6e8;
    --paper: #ffffff;
    --stage: #f4f4f4;
  }
  * { box-sizing: border-box; margin: 0; padding: 0; }
  html, body { width: 1200px; height: 1200px; overflow: hidden; }
  body {
    background: var(--stage);
    font-family: "Montserrat", Arial, sans-serif;
    color: var(--ink);
    position: relative;
  }

  /* ---------- bottle label (flat) ---------- */
  .label {
    position: absolute; left: 70px; top: 330px;
    width: 360px; height: 560px;
    background: var(--paper);
    border-left: 24px solid var(--charcoal);
    border-right: 24px solid var(--charcoal);
    box-shadow: 0 2px 8px rgba(0,0,0,.08);
  }
  .label .brand {
    position: absolute; top: 46px; left: 0; right: 0;
    display: flex; align-items: center; justify-content: center; gap: 10px;
    font-weight: 700; font-size: 24px; letter-spacing: 2px;
    color: var(--ink); text-transform: uppercase;
  }
  .brand .dot { width: 14px; height: 14px; border-radius: 50%; background: var(--charcoal); }
  .label .product {
    position: absolute; top: 108px; left: 24px;
    font-size: 60px; color: var(--charcoal); line-height: 1; white-space: nowrap;
  }
  .product b { font-weight: 800; }
  .product span { font-weight: 300; }
  .label .strength {
    position: absolute; left: 18px; top: 520px;
    transform: rotate(-90deg); transform-origin: left top;
    font-weight: 700; font-size: 62px; line-height: 1; color: var(--charcoal);
    letter-spacing: -1px; white-space: nowrap;
  }
  .label .molecule {
    position: absolute; left: 110px; top: 250px; width: 190px; height: 250px;
    background: radial-gradient(circle at 40% 45%, var(--pale-grey), rgba(230,230,232,0) 70%);
  }

  /* ---------- box front panel ---------- */
  .box-front {
    position: absolute; left: 490px; top: 100px;
    width: 420px; height: 1000px;
    background: var(--paper);
    box-shadow: 0 2px 8px rgba(0,0,0,.08);
    overflow: hidden;
  }
  .box-front .title {
    position: absolute; left: 300px; top: 380px;
    transform: rotate(-90deg); transform-origin: left top;
    font-size: 88px; color: var(--charcoal); line-height: 1; white-space: nowrap;
  }
  .box-front .title b { font-weight: 800; }
  .box-front .title span { font-weight: 300; }
  .box-front .molecule {
    position: absolute; left: 100px; top: 440px; width: 270px; height: 240px;
    background: radial-gradient(circle at 45% 50%, var(--pale-grey), rgba(230,230,232,0) 70%);
  }
  .box-front .band {
    position: absolute; left: 0; right: 0; top: 690px; height: 250px;
    background: var(--charcoal);
    display: flex; align-items: center; justify-content: center; gap: 14px;
  }
  .band .brand {
    font-weight: 700; font-size: 34px; letter-spacing: 3px; line-height: 1;
    color: var(--paper); text-transform: uppercase; white-space: nowrap;
  }
  .band .dot { width: 18px; height: 18px; border-radius: 50%; background: var(--paper); flex: none; }
  .box-front .strength {
    position: absolute; left: 50px; top: 946px;
    font-weight: 600; font-size: 48px; color: var(--ink); line-height: 1;
  }
  .strength small { font-size: 30px; }

  /* ---------- box side panel ---------- */
  .box-side {
    position: absolute; left: 910px; top: 100px;
    width: 220px; height: 1000px;
    background: #f7f7f7;
    border-left: 1px solid #dcdcdc;
    box-shadow: 0 2px 8px rgba(0,0,0,.08);
  }
  .box-side .info { position: absolute; top: 110px; left: 22px; right: 22px; font-size: 10.5px; line-height: 1.55; color: #555; }
  .info h2 { font-size: 11px; font-weight: 700; text-transform: uppercase; letter-spacing: 1px; margin-bottom: 12px; text-align: center; color: var(--ink); }
  .info p { margin-bottom: 14px; }
  .box-side .band {
    position: absolute; left: 0; right: 0; top: 690px; height: 250px;
    background: var(--charcoal);
  }
  .box-side .band .mark {
    position: absolute; left: 0; right: 0; bottom: 40px;
    display: flex; align-items: center; justify-content: center; gap: 6px;
  }
  .box-side .band .brand { font-size: 13px; letter-spacing: 1.5px; }
  .box-side .band .dot { width: 8px; height: 8px; }
</style>
</head>
<body>

  <section class="label" aria-label="Bottle label">
    <div class="brand"><i class="dot"></i>Meridell CBD</div>
    <h1 class="product"><b>CBD</b> <span>Oil</span></h1>
    <div class="strength">1000mg</div>
    <div class="molecule" role="img" aria-label="Soft grey hexagon molecule pattern"></div>
  </section>

  <section class="box-front" aria-label="Box front panel">
    <h1 class="title"><b>CBD</b> <span>Oil</span></h1>
    <div class="molecule" role="img" aria-label="Soft grey hexagon molecule pattern"></div>
    <div class="band"><i class="dot"></i><span class="brand">Meridell CBD</span></div>
    <div class="strength">1000<small>mg</small></div>
  </section>

  <section class="box-side" aria-label="Box side panel">
    <div class="info">
      <h2>About our oils</h2>
      <p>Our oils are made from organically grown European hemp, gently extracted to keep the full range of natural plant compounds. Each batch is tested by an independent lab for purity and strength.</p>
      <p>Shake well before use. Place drops under the tongue and hold for sixty seconds. Store in a cool, dark place away from children.</p>
    </div>
    <div class="band"><div class="mark"><i class="dot"></i><span class="brand">Meridell CBD</span></div></div>
  </section>

</body>
</html>
```